Business card for Crestline Bathrooms

Please design a business card for our bathroom renovation business. You can use my existing logo, but if you have an idea to modernize it, I would like to see it. Please see attached files first. I would like to use the blue and the orange theme. I like the concept of using the shower head in the logo. Please find following a design (or two) that I have been trying to create with my limited resources. That design was for a sign, but I was going to adopt it and use it as a business card as well. I like the concept of the water splash but I don’t think it “flows” nicely together with the logo. Another thought is that maybe creating the logo out of water splash could work and have a dramatic effect (like the water text and the butterfly picture attached with similar background instead of white). If the above doesn’t work I would like to see a modern simplified design. One of the attached files named as the unwanted business card has all the details that I want included in the business card. Please note that it is two sided.
Updates

I am very thankful for the designs that I have received, but they are very similar and only a couple of attempts to do something with the water splash as per my original brief. Modernizing the logo and having it made out of out of water splash with the orange as color accent could work and have a dramatic effect (like the water text and the butterfly picture attached with similar background instead of white). Please do not use the butterfly itself! This is just an example that images can be created out of water splash.

Contact Information for Business Card

all the details are on the unwonted business card file included

Colors
3176b5

Requirements
Nice to have
• Copied from the brief:
• ... maybe creating the logo out of water splash could work and have a dramatic effect (like the water text and the butterfly picture attached with similar background instead of white). Please do not use the butterfly itself!
Should not have
• I am getting designs with a butterfly. The butterfly picture was an example of creating something from a water splash. The butterfly itself has no association with anything other than the concept of creating a logo out of water splash. Sorry, I thought I was clear in the brief.

```html
<!DOCTYPE html>
<html lang="en">
<head>
<meta charset="utf-8">
<title>Crestline Bathrooms – Business Card</title>
<link href="https://fonts.googleapis.com/css2?family=Questrial&family=Arimo:wght@400;700&display=swap" rel="stylesheet">
<style>
  :root {
    --backdrop: #8c8c8c;
    --card-white: #f6f7f8;
    --navy: #0e426b;
    --navy-deep: #0a3a60;
    --coral: #ec7463;
    --ink: #2b2b2b;
    --splash-light: #d7e4ee;
    --splash-soft: #eef3f7;
    --badge-green: #3aa935;
    --badge-orange: #f2a31b;
  }
  * { box-sizing: border-box; margin: 0; padding: 0; }
  html, body { width: 1200px; height: 1200px; overflow: hidden; }
  body {
    background: var(--backdrop);
    position: relative;
    font-family: "Arimo", Arial, sans-serif;
  }
  .card {
    position: absolute;
    top: 310px;
    height: 594px;
    box-shadow: 3px 4px 6px rgba(0,0,0,0.35);
    overflow: hidden;
  }
  .card--front { left: 234px; width: 364px; background: var(--card-white); }
  .card--back { left: 627px; width: 370px; background: var(--navy); }

  .splash-art {
    position: absolute;
    inset: 0;
    background:
      radial-gradient(ellipse 60% 30% at 70% 12%, var(--splash-light), transparent 70%),
      radial-gradient(ellipse 80% 35% at 45% 55%, var(--splash-light), transparent 70%),
      radial-gradient(ellipse 70% 25% at 60% 88%, var(--splash-soft), transparent 70%);
  }
  .splash-art--dark {
    inset: auto 0 0 0;
    height: 300px;
    background: radial-gradient(ellipse 70% 50% at 50% 75%, rgba(80,130,175,0.35), transparent 75%);
  }

  .brand {
    position: absolute;
    display: flex;
    align-items: center;
    gap: 16px;
  }
  .brand__mark {
    width: 74px; height: 74px;
    border: 3px solid currentColor;
    flex: none;
  }
  .brand__name {
    font-family: "Questrial", Arial, sans-serif;
    font-weight: 400;
    line-height: 1;
  }
  .brand__word { display: block; font-size: 40px; letter-spacing: 0.5px; }
  .brand__sub { display: block; font-size: 20px; margin-top: 6px; text-align: right; }
  .card--front .brand { top: 115px; left: 34px; color: var(--navy); }
  .card--back .brand { top: 146px; left: 38px; color: #fff; }

  .contact {
    position: absolute;
    left: 0; right: 0;
    top: 292px;
    text-align: center;
    color: var(--ink);
  }
  .contact__name {
    font-weight: 700;
    font-size: 21px;
    color: var(--navy);
    letter-spacing: 0.3px;
  }
  .contact__name span { color: var(--coral); }
  .divider {
    width: 204px; height: 3px;
    margin: 12px auto;
    background: repeating-linear-gradient(90deg, var(--coral) 0 9px, transparent 9px 14px, var(--navy) 14px 23px, transparent 23px 28px);
  }
  .contact__lines { font-size: 16.5px; line-height: 21.5px; }
  .contact__lines b { color: var(--navy); }
  .contact__address { margin-top: 18px; font-size: 16.5px; }

  .badges {
    position: absolute;
    top: 510px; left: 66px;
    display: flex; align-items: center; gap: 14px;
  }
  .badge--round { width: 46px; height: 54px; border-radius: 12px; background: var(--badge-green); }
  .badge--block { width: 178px; height: 44px; display: flex; gap: 8px; align-items: center; }
  .badge--block i { width: 36px; height: 40px; background: var(--badge-orange); display: block; }
  .badge--block em { flex: 1; height: 14px; background: var(--navy); display: block; }

  .services {
    position: absolute;
    top: 371px; left: 0; right: 0;
    text-align: center;
    color: #fff;
    font-size: 15.5px;
    line-height: 24.5px;
    text-transform: uppercase;
  }
</style>
</head>
<body>
  <section class="card card--front">
    <div class="splash-art" role="img" aria-label="Pale blue water splash flowing across the card"></div>
    <div class="brand">
      <div class="brand__mark"></div>
      <div class="brand__name">
        <span class="brand__word">Crestline</span>
        <span class="brand__sub">Bathrooms</span>
      </div>
    </div>
    <div class="contact">
      <p class="contact__name">DANIEL <span>MORAVEC</span></p>
      <div class="divider"></div>
      <div class="contact__lines">
        <p><b>P:</b> 0400 318 274</p>
        <p><b>M:</b> 6200 4417</p>
        <p><b>E:</b> daniel@crestlinebathrooms.com.au</p>
        <p><b>W:</b> crestlinebathrooms.com.au</p>
      </div>
      <div class="divider"></div>
      <p class="contact__address">PO Box 41 Hollydale 2620</p>
    </div>
    <div class="badges">
      <div class="badge--round" aria-label="Industry association badge"></div>
      <div class="badge--block" aria-label="Builders association badge"><i></i><em></em></div>
    </div>
  </section>

  <section class="card card--back">
    <div class="splash-art splash-art--dark" role="img" aria-label="Faint water splash in a bath at the bottom of the card"></div>
    <div class="brand">
      <div class="brand__mark"></div>
      <div class="brand__name">
        <span class="brand__word">Crestline</span>
        <span class="brand__sub">Bathrooms</span>
      </div>
    </div>
    <div class="services">
      <p>Complete Bathroom</p>
      <p>Renovations &amp; Remodelling</p>
      <p>Highly Skilled &amp; Qualified</p>
      <p>Tradespeople</p>
      <p>Professional Service From</p>
      <p>Concept to Completion</p>
      <p>All Work Guaranteed</p>
    </div>
  </section>
</body>
</html>
```